VOXterra Roadmap for developing engineer 3D-BIM-projects over a longer period of time

We need functional and scalable PowerPoint templates with four main slides. The design should be carried out in the context of the enclosed documents; or at least in this sense.
As engineers, we develop projects over a longer period of time. To visualize topics along the way (downside timeline) and goals (upside timeline) for our customers (and for us), we need an overview for the project management in sort of a roadmap.
Our design requirements are simplicity, clarity and accuracy. These are also the service requirements for our customers.
As always, it's urgent. Our goal is to select the design by Wednesday November 10th and make any adjustments with the winner by Friday November 12th.

Target Market(s)

Architects, Engineers, World Heritage; 3D-Modelling, BIM Building Information Modeling

Industry/Entity Type

World Heritage Buildings and Objects

Requirements
Must have
• simplicity, logic, elegant (see the attached documents)
Nice to have
• see the attached documents

```html
<!DOCTYPE html>
<html lang="en">
<head>
<meta charset="utf-8">
<title>VOXterra Roadmap Templates</title>
<link href="https://fonts.googleapis.com/css2?family=Montserrat:wght@400;500;600;700;800&display=swap" rel="stylesheet">
<style>
  :root{
    --bg:#f1f1f2;
    --white:#ffffff;
    --red:#e3371e;
    --red-soft:#f1917f;
    --blue:#0b5cad;
    --blue-line:#5b8fd6;
    --ink:#1b1b1b;
    --text:#3d3d3d;
    --muted:#8a8a8a;
    --faint:#cfcfcf;
    --dot:#dcdcdc;
  }
  *{margin:0;padding:0;box-sizing:border-box}
  html,body{width:1200px;height:716px;overflow:hidden;background:var(--bg)}
  body{position:relative;font-family:"Montserrat",sans-serif;color:var(--text)}

  .slide{position:absolute;width:375px;height:211px;background:var(--white);box-shadow:0 1px 3px rgba(0,0,0,.12);overflow:hidden}
  .abs{position:absolute}

  /* cover */
  .cover-logo{position:absolute;left:133px;top:29px;width:110px;height:51px;background:var(--white);border-radius:6px;box-shadow:0 2px 8px rgba(0,0,0,.12);display:flex;align-items:center;justify-content:center;gap:5px}
  .brand-square{width:8px;height:8px;background:var(--red)}
  .brand-small{font-weight:800;font-size:17px;color:var(--red);letter-spacing:-.2px}
  .cover-title{position:absolute;left:0;right:0;top:116px;text-align:center;font-weight:800;font-size:12.5px;color:var(--ink)}
  .cover-sub{position:absolute;left:0;right:0;top:141px;text-align:center;font-weight:700;font-size:9.4px;color:var(--faint)}

  /* brand showcase */
  .brand-large{position:absolute;left:511px;top:82px;display:flex;align-items:center;gap:10px}
  .brand-large .brand-square{width:22px;height:22px}
  .brand-large-name{font-weight:800;font-size:46px;color:var(--blue);letter-spacing:-1px}

  /* button showcase */
  .demo-circle{position:absolute;width:111px;height:111px;border-radius:50%;background:var(--white);box-shadow:0 2px 10px rgba(0,0,0,.05)}
  .demo-circle.arrow{left:805px;top:56px;background:#f7f7f8}
  .demo-square{position:absolute;left:20px;top:18px;width:70px;height:70px;border-radius:8px;background:var(--white);box-shadow:0 3px 10px rgba(0,0,0,.08);display:flex;align-items:center;justify-content:center}
  .demo-circle.month{left:1034px;top:56px}
  .demo-month-label{position:absolute;left:0;right:0;top:25px;text-align:center;font-size:15px;font-weight:500;color:var(--ink)}
  .demo-track{position:absolute;left:1px;right:1px;top:65px;height:4px;background:var(--red-soft)}
  .demo-knob{position:absolute;left:38px;top:48px;width:35px;height:35px;border-radius:50%;background:#d6d6d6;border:4px solid var(--white);box-shadow:0 3px 6px rgba(0,0,0,.2)}
  .demo-caption{position:absolute;left:790px;width:370px;top:196px;text-align:center;font-size:14.6px;font-weight:500;color:var(--ink);letter-spacing:.2px}

  /* nav button */
  .nav-btn{position:absolute;width:21px;height:21px;background:var(--white);border-radius:3px;box-shadow:0 1px 4px rgba(0,0,0,.12);display:flex;align-items:center;justify-content:center}
  .nav-btn svg{width:8px;height:8px}

  /* month timeline */
  .timeline{position:absolute;left:36.4px;width:303.3px;height:14px}
  .timeline-line{position:absolute;left:12.6px;right:12.6px;height:1px;background:var(--red-soft)}
  .timeline-months{position:absolute;inset:0;display:flex}
  .month{position:relative;flex:1}
  .month-label{position:absolute;left:0;right:0;text-align:center;font-size:3.6px;font-weight:600;color:var(--ink)}
  .month-dot{position:absolute;left:50%;width:6px;height:6px;margin-left:-3px;border-radius:50%;background:var(--dot);box-shadow:0 0 0 1px var(--white),0 1px 2px rgba(0,0,0,.2)}
  .month-dot.active{background:var(--red)}
  .timeline.top .timeline-line{top:11.5px}
  .timeline.top .month-label{top:2px}
  .timeline.top .month-dot{top:9px}
  .timeline.bottom .timeline-line{top:3.5px}
  .timeline.bottom .month-dot{top:1px}
  .timeline.bottom .month-label{top:9.5px}

  /* content card */
  .content-card{position:absolute;left:7px;width:361px;background:var(--white);box-shadow:0 1px 4px rgba(0,0,0,.1)}
  .content-list{list-style:none;font-size:7.2px;line-height:12.6px;color:var(--text)}
  .content-list.marked li{position:relative;padding-left:8px}
  .content-list.marked li::before{content:"";position:absolute;left:0;top:4.5px;border-left:3px solid var(--red);border-top:2px solid transparent;border-bottom:2px solid transparent}

  .project-heading{position:absolute;font-size:7.1px;font-weight:700;color:var(--blue)}
  .project-month{position:absolute;font-size:7.1px;font-weight:500;color:var(--blue)}
  .meta{position:absolute;font-size:4.4px;font-weight:500;color:var(--muted);transform:translateX(-50%)}

  /* gallery slide */
  .photo{position:absolute;top:15px;width:67px;height:67px;border-radius:2px;box-shadow:0 2px 5px rgba(0,0,0,.2)}
  .photo.sky{background:linear-gradient(160deg,#3d7cc9 0%,#9fc1e3 45%,#1d3f6c 70%,#0c1f3a 100%)}
  .photo.houses{background:linear-gradient(180deg,#56c6c8 0%,#7fd6d6 55%,#c9d6d8 80%,#3a4448 100%)}
  .photo.glass{background:linear-gradient(135deg,#0e2d6a 0%,#2f63b5 45%,#6d9be0 60%,#0b2152 100%)}
  .gallery-line{position:absolute;left:0;right:0;top:90px;height:1px;background:var(--red)}
  .gallery-dot{position:absolute;top:87px;width:6px;height:6px;margin-left:-3px;border-radius:50%;background:var(--dot);box-shadow:0 0 0 1px var(--white),0 1px 2px rgba(0,0,0,.2)}
  .gallery-dot.active{background:var(--red)}
  .month-tag{position:absolute;top:101px;width:53px;height:12px;margin-left:-26.5px;background:var(--white);box-shadow:0 1px 3px rgba(0,0,0,.1);font-size:5.3px;font-weight:500;color:var(--ink);text-align:center;line-height:12px}
  .gallery-title{position:absolute;left:0;right:0;top:130px;text-align:center;font-size:6.9px;font-weight:700;color:var(--ink)}
  .gallery-rule{position:absolute;left:55px;width:275px;top:142px;height:1px;background:linear-gradient(90deg,rgba(91,143,214,0),var(--blue-line) 20%,var(--blue-line) 80%,rgba(91,143,214,0))}
  .gallery-list{position:absolute;left:47px;top:146px;list-style:none;font-size:6.2px;line-height:11.2px;color:var(--ink)}
  .gallery-list li{position:relative;padding-left:8px}
  .gallery-list li::before{content:"";position:absolute;left:0;top:4px;border-left:2.5px solid var(--red);border-top:1.6px solid transparent;border-bottom:1.6px solid transparent}
  .gallery-text{position:absolute;left:47px;width:281px;top:146px;font-size:6.2px;line-height:11.2px;color:var(--ink)}
</style>
</head>
<body>

<!-- Cover slide -->
<section class="slide" style="left:18px;top:26px">
  <div class="cover-logo"><span class="brand-square"></span><span class="brand-small">VOXterra</span></div>
  <h1 class="cover-title">PROJECT NAME HERE</h1>
  <p class="cover-sub">Lorem ipsum dolor sit amet consectetur adipisicing elit</p>
</section>

<!-- Brand mark -->
<div class="brand-large"><span class="brand-square"></span><span class="brand-large-name">VOXterra</span></div>

<!-- Button showcase -->
<div class="demo-circle arrow">
  <div class="demo-square">
    <svg width="20" height="20" viewBox="0 0 20 20" fill="none" stroke="#1b1b1b" stroke-width="1.8" stroke-linecap="round" stroke-linejoin="round"><path d="M2 10h16M11 3l7 7-7 7"/></svg>
  </div>
</div>
<div class="demo-circle month">
  <div class="demo-month-label">SEPT</div>
  <div class="demo-track"></div>
  <div class="demo-knob"></div>
</div>
<p class="demo-caption">CLICKABLE BUTTONS FOR EASY NAVIGATION</p>

<!-- Row 2, slide 1: timeline top, bullets -->
<section class="slide" style="left:18px;top:251px">
  <div class="nav-btn" style="left:8px;top:8px"><svg viewBox="0 0 10 10" fill="none" stroke="#1b1b1b" stroke-width="1.2"><path d="M9 5H1M4 2L1 5l3 3"/></svg></div>
  <div class="timeline top" style="top:6px">
    <div class="timeline-line"></div>
    <div class="timeline-months">
      <div class="month"><span class="month-label">JAN</span><span class="month-dot active"></span></div>
      <div class="month"><span class="month-label">FEB</span><span class="month-dot"></span></div>
      <div class="month"><span class="month-label">MAR</span><span class="month-dot"></span></div>
      <div class="month"><span class="month-label">APR</span><span class="month-dot"></span></div>
      <div class="month"><span class="month-label">MAY</span><span class="month-dot"></span></div>
      <div class="month"><span class="month-label">JUN</span><span class="month-dot"></span></div>
      <div class="month"><span class="month-label">JUL</span><span class="month-dot"></span></div>
      <div class="month"><span class="month-label">AUG</span><span class="month-dot"></span></div>
      <div class="month"><span class="month-label">SEPT</span><span class="month-dot"></span></div>
      <div class="month"><span class="month-label">OCT</span><span class="month-dot"></span></div>
      <div class="month"><span class="month-label">NOV</span><span class="month-dot"></span></div>
      <div class="month"><span class="month-label">DEC</span><span class="month-dot"></span></div>
    </div>
  </div>
  <div class="nav-btn" style="left:347px;top:8px"><svg viewBox="0 0 10 10" fill="none" stroke="#1b1b1b" stroke-width="1.2"><path d="M1 5h8M6 2l3 3-3 3"/></svg></div>
  <div class="content-card" style="top:37px;height:136px">
    <ul class="content-list marked" style="position:absolute;left:20px;top:13px">
      <li>Content here</li>
      <li>Lorem ipsum dolor sit amet consectetur adipisicing elit.</li>
      <li>Dicta, nihil totam. Laborum, quo.</li>
      <li>Necessitatibus cupiditate eveniet veritatis error officiis soluta aperiam.</li>
      <li>Consequatur, quos similique, ad earum laboriosam eveniet aspernatur.</li>
      <li>Porro impedit enim nam placeat incidunt mollitia sed.</li>
      <li>Sed labore provident maxime, voluptatum.</li>
      <li>Cum non eveniet quia earum minima porro possimus!</li>
    </ul>
  </div>
  <p class="project-heading" style="left:16px;top:187px">YOUR PROJECT NAME DONE IN JAN</p>
  <p class="project-month" style="right:16px;top:187px">JAN</p>
  <p class="meta" style="left:125px;top:201px">ROADMAP</p>
  <p class="meta" style="left:258px;top:201px">2021</p>
</section>

<!-- Row 2, slide 2: gallery with bullets -->
<section class="slide" style="left:405px;top:251px">
  <div class="photo sky" style="left:37px" role="img" aria-label="Photo of a glass tower against a blue sky"></div>
  <div class="photo houses" style="left:154px" role="img" aria-label="Photo of a row of gabled houses under a turquoise sky"></div>
  <div class="photo glass" style="left:271px" role="img" aria-label="Photo of an angular blue glass facade"></div>
  <div class="nav-btn" style="left:7px;top:38px"><svg viewBox="0 0 10 10" fill="none" stroke="#1b1b1b" stroke-width="1.2"><path d="M9 5H1M4 2L1 5l3 3"/></svg></div>
  <div class="nav-btn" style="left:346px;top:38px"><svg viewBox="0 0 10 10" fill="none" stroke="#1b1b1b" stroke-width="1.2"><path d="M1 5h8M6 2l3 3-3 3"/></svg></div>
  <div class="gallery-line"></div>
  <span class="gallery-dot" style="left:71px"></span>
  <span class="gallery-dot active" style="left:187px"></span>
  <span class="gallery-dot" style="left:305px"></span>
  <span class="month-tag" style="left:70px">DECEMBER</span>
  <span class="month-tag" style="left:187px">JANUARY</span>
  <span class="month-tag" style="left:304px">FEBRUARY</span>
  <h2 class="gallery-title">PROJECT TITLE HERE</h2>
  <div class="gallery-rule"></div>
  <ul class="gallery-list">
    <li>Lorem ipsum dolor sit amet consectetur adipisicing elit.</li>
    <li>Dicta, nihil totam.</li>
    <li>Necessitatibus cupiditate eveniet veritatis error officiis soluta aperiam.</li>
    <li>Consequatur.</li>
  </ul>
  <p class="meta" style="left:125px;top:200px">ROADMAP</p>
  <p class="meta" style="left:258px;top:200px">2021</p>
</section>

<!-- Row 2, slide 3: timeline bottom, bullets -->
<section class="slide" style="left:793px;top:251px">
  <p class="project-heading" style="left:16px;top:12px">YOUR PROJECT NAME DONE IN JAN</p>
  <p class="project-month" style="right:16px;top:12px">JAN</p>
  <div class="content-card" style="top:27px;height:135px">
    <ul class="content-list marked" style="position:absolute;left:20px;top:16px">
      <li>Content here</li>
      <li>Lorem ipsum dolor sit amet consectetur adipisicing elit.</li>
      <li>Dicta, nihil totam. Laborum, quo.</li>
      <li>Necessitatibus cupiditate eveniet veritatis error officiis soluta aperiam.</li>
      <li>Consequatur, quos similique, ad earum laboriosam eveniet aspernatur.</li>
      <li>Porro impedit enim nam placeat incidunt mollitia sed.</li>
      <li>Sed labore provident maxime, voluptatum.</li>
      <li>Cum non eveniet quia earum minima porro possimus!</li>
    </ul>
  </div>
  <div class="nav-btn" style="left:8px;top:175px"><svg viewBox="0 0 10 10" fill="none" stroke="#1b1b1b" stroke-width="1.2"><path d="M9 5H1M4 2L1 5l3 3"/></svg></div>
  <div class="timeline bottom" style="top:181px">
    <div class="timeline-line"></div>
    <div class="timeline-months">
      <div class="month"><span class="month-dot active"></span><span class="month-label">JAN</span></div>
      <div class="month"><span class="month-dot"></span><span class="month-label">FEB</span></div>
      <div class="month"><span class="month-dot"></span><span class="month-label">MAR</span></div>
      <div class="month"><span class="month-dot"></span><span class="month-label">APR</span></div>
      <div class="month"><span class="month-dot"></span><span class="month-label">MAY</span></div>
      <div class="month"><span class="month-dot"></span><span class="month-label">JUN</span></div>
      <div class="month"><span class="month-dot"></span><span class="month-label">JUL</span></div>
      <div class="month"><span class="month-dot"></span><span class="month-label">AUG</span></div>
      <div class="month"><span class="month-dot"></span><span class="month-label">SEPT</span></div>
      <div class="month"><span class="month-dot"></span><span class="month-label">OCT</span></div>
      <div class="month"><span class="month-dot"></span><span class="month-label">NOV</span></div>
      <div class="month"><span class="month-dot"></span><span class="month-label">DEC</span></div>
    </div>
  </div>
  <div class="nav-btn" style="left:347px;top:175px"><svg viewBox="0 0 10 10" fill="none" stroke="#1b1b1b" stroke-width="1.2"><path d="M1 5h8M6 2l3 3-3 3"/></svg></div>
  <p class="meta" style="left:124px;top:202px">ROADMAP</p>
  <p class="meta" style="left:258px;top:202px">2021</p>
</section>

<!-- Row 3, slide 1: timeline top, plain lines -->
<section class="slide" style="left:18px;top:477px">
  <div class="nav-btn" style="left:8px;top:8px"><svg viewBox="0 0 10 10" fill="none" stroke="#1b1b1b" stroke-width="1.2"><path d="M9 5H1M4 2L1 5l3 3"/></svg></div>
  <div class="timeline top" style="top:6px">
    <div class="timeline-line"></div>
    <div class="timeline-months">
      <div class="month"><span class="month-label">JAN</span><span class="month-dot active"></span></div>
      <div class="month"><span class="month-label">FEB</span><span class="month-dot"></span></div>
      <div class="month"><span class="month-label">MAR</span><span class="month-dot"></span></div>
      <div class="month"><span class="month-label">APR</span><span class="month-dot"></span></div>
      <div class="month"><span class="month-label">MAY</span><span class="month-dot"></span></div>
      <div class="month"><span class="month-label">JUN</span><span class="month-dot"></span></div>
      <div class="month"><span class="month-label">JUL</span><span class="month-dot"></span></div>
      <div class="month"><span class="month-label">AUG</span><span class="month-dot"></span></div>
      <div class="month"><span class="month-label">SEPT</span><span class="month-dot"></span></div>
      <div class="month"><span class="month-label">OCT</span><span class="month-dot"></span></div>
      <div class="month"><span class="month-label">NOV</span><span class="month-dot"></span></div>
      <div class="month"><span class="month-label">DEC</span><span class="month-dot"></span></div>
    </div>
  </div>
  <div class="nav-btn" style="left:347px;top:8px"><svg viewBox="0 0 10 10" fill="none" stroke="#1b1b1b" stroke-width="1.2"><path d="M1 5h8M6 2l3 3-3 3"/></svg></div>
  <div class="content-card" style="top:37px;height:136px">
    <ul class="content-list" style="position:absolute;left:19px;top:13px">
      <li>Content here</li>
      <li>Lorem ipsum dolor sit amet consectetur adipisicing elit.</li>
      <li>Dicta, nihil totam. Laborum, quo.</li>
      <li>Necessitatibus cupiditate eveniet veritatis error officiis soluta aperiam.</li>
      <li>Consequatur, quos similique, ad earum laboriosam eveniet aspernatur.</li>
      <li>Porro impedit enim nam placeat incidunt mollitia sed.</li>
      <li>Sed labore provident maxime, voluptatum.</li>
      <li>Cum non eveniet quia earum minima porro possimus!</li>
    </ul>
  </div>
  <p class="project-heading" style="left:16px;top:187px">YOUR PROJECT NAME DONE IN JAN</p>
  <p class="project-month" style="right:16px;top:187px">JAN</p>
  <p class="meta" style="left:125px;top:201px">ROADMAP</p>
  <p class="meta" style="left:258px;top:201px">2021</p>
</section>

<!-- Row 3, slide 2: gallery with paragraph -->
<section class="slide" style="left:405px;top:477px">
  <div class="photo sky" style="left:37px" role="img" aria-label="Photo of a glass tower against a blue sky"></div>
  <div class="photo houses" style="left:154px" role="img" aria-label="Photo of a row of gabled houses under a turquoise sky"></div>
  <div class="photo glass" style="left:271px" role="img" aria-label="Photo of an angular blue glass facade"></div>
  <div class="nav-btn" style="left:7px;top:38px"><svg viewBox="0 0 10 10" fill="none" stroke="#1b1b1b" stroke-width="1.2"><path d="M9 5H1M4 2L1 5l3 3"/></svg></div>
  <div class="nav-btn" style="left:346px;top:38px"><svg viewBox="0 0 10 10" fill="none" stroke="#1b1b1b" stroke-width="1.2"><path d="M1 5h8M6 2l3 3-3 3"/></svg></div>
  <div class="gallery-line"></div>
  <span class="gallery-dot" style="left:71px"></span>
  <span class="gallery-dot active" style="left:187px"></span>
  <span class="gallery-dot" style="left:305px"></span>
  <span class="month-tag" style="left:70px">DECEMBER</span>
  <span class="month-tag" style="left:187px">JANUARY</span>
  <span class="month-tag" style="left:304px">FEBRUARY</span>
  <h2 class="gallery-title">PROJECT TITLE HERE</h2>
  <div class="gallery-rule"></div>
  <p class="gallery-text" style="left:47px">Lorem ipsum dolor sit amet consectetur adipisicing elit. Dicta, nihil totam. Laborum, quo. Necessitatibus cupiditate eveniet veritatis error officiis soluta aperiam. Consequatur, quos similique, ad earum laboriosam eveniet aspernatur porro impedit enim placeat incident sed.</p>
  <p class="meta" style="left:125px;top:200px">ROADMAP</p>
  <p class="meta" style="left:258px;top:200px">2021</p>
</section>

<!-- Row 3, slide 3: timeline bottom, plain lines -->
<section class="slide" style="left:793px;top:477px">
  <p class="project-heading" style="left:16px;top:12px">YOUR PROJECT NAME DONE IN JAN</p>
  <p class="project-month" style="right:16px;top:12px">JAN</p>
  <div class="content-card" style="top:27px;height:135px">
    <ul class="content-list" style="position:absolute;left:19px;top:16px">
      <li>Content here</li>
      <li>Lorem ipsum dolor sit amet consectetur adipisicing elit.</li>
      <li>Dicta, nihil totam. Laborum, quo.</li>
      <li>Necessitatibus cupiditate eveniet veritatis error officiis soluta aperiam.</li>
      <li>Consequatur, quos similique, ad earum laboriosam eveniet aspernatur.</li>
      <li>Porro impedit enim nam placeat incidunt mollitia sed.</li>
      <li>Sed labore provident maxime, voluptatum.</li>
      <li>Cum non eveniet quia earum minima porro possimus!</li>
    </ul>
  </div>
  <div class="nav-btn" style="left:8px;top:175px"><svg viewBox="0 0 10 10" fill="none" stroke="#1b1b1b" stroke-width="1.2"><path d="M9 5H1M4 2L1 5l3 3"/></svg></div>
  <div class="timeline bottom" style="top:181px">
    <div class="timeline-line"></div>
    <div class="timeline-months">
      <div class="month"><span class="month-dot active"></span><span class="month-label">JAN</span></div>
      <div class="month"><span class="month-dot"></span><span class="month-label">FEB</span></div>
      <div class="month"><span class="month-dot"></span><span class="month-label">MAR</span></div>
      <div class="month"><span class="month-dot"></span><span class="month-label">APR</span></div>
      <div class="month"><span class="month-dot"></span><span class="month-label">MAY</span></div>
      <div class="month"><span class="month-dot"></span><span class="month-label">JUN</span></div>
      <div class="month"><span class="month-dot"></span><span class="month-label">JUL</span></div>
      <div class="month"><span class="month-dot"></span><span class="month-label">AUG</span></div>
      <div class="month"><span class="month-dot"></span><span class="month-label">SEPT</span></div>
      <div class="month"><span class="month-dot"></span><span class="month-label">OCT</span></div>
      <div class="month"><span class="month-dot"></span><span class="month-label">NOV</span></div>
      <div class="month"><span class="month-dot"></span><span class="month-label">DEC</span></div>
    </div>
  </div>
  <div class="nav-btn" style="left:347px;top:175px"><svg viewBox="0 0 10 10" fill="none" stroke="#1b1b1b" stroke-width="1.2"><path d="M1 5h8M6 2l3 3-3 3"/></svg></div>
  <p class="meta" style="left:124px;top:202px">ROADMAP</p>
  <p class="meta" style="left:258px;top:202px">2021</p>
</section>

</body>
</html>
```